TKB Roofing Flyer/Mailer to be used to market to Homeowners

We need to create a flyer than can double as a mailer for our roofing business and possibly be used as a door hanger as well. This flyer will advertise our roofing company in a professional way with pictures as well as clear and precise text about who we are and what we offer. We are open to this flyer being a bi-fold or even a tri-fold. There would need to be an area for address if used as a mailer. A majority of our company information can be found on our website at www.tkbroofing-example.com.

Target Market(s)

Home Owners

Industry/Entity Type

Construction

Colors
0255a3
ffffff

Requirements
Must have
• Professional design, pictures, text with info regarding our company. Website: www.tkbroofing-example.com

```html
<!DOCTYPE html>
<html lang="en">
<head>
<meta charset="utf-8">
<title>TKB Roofing Tri-Fold Mailer</title>
<link rel="stylesheet" href="https://fonts.googleapis.com/css2?family=Open+Sans:wght@400;600;700&family=Arimo:wght@400;700&family=Tinos:wght@700&display=swap">
<style>
  :root{
    --blue:#0d4ba6;
    --navy:#0a3a8c;
    --ink:#1c3f8e;
    --cyan:#0a96dd;
    --pale:#cdd8ec;
    --white:#ffffff;
    --stage:#b9babb;
  }
  *{box-sizing:border-box;margin:0;padding:0}
  html,body{width:1200px;height:1170px;overflow:hidden}
  body{background:radial-gradient(ellipse at 50% 52%,#e2e2e2 0%,#c6c7c8 45%,var(--stage) 100%);font-family:"Open Sans",sans-serif;position:relative}
  .sheet{position:absolute;background:var(--white);box-shadow:0 0 0 1px #8d8f92;overflow:hidden}
  .sheet svg.art{position:absolute;inset:0}
  .outside{left:177px;top:101px;width:863px;height:490px}
  .inside{left:162px;top:620px;width:882px;height:500px}
  .txt{position:absolute}

  /* outside: left panel */
  .intro{left:18px;top:252px;width:262px;font-size:10.2px;line-height:14.8px;color:var(--ink);text-transform:uppercase}
  .intro ul{list-style:none;font-weight:700}
  .intro-note{left:18px;top:390px;width:262px;font-size:10.2px;line-height:14.8px;color:var(--ink);text-transform:uppercase}

  /* outside: cover contact panel */
  .brand{left:288px;top:34px;width:287px;text-align:center;color:var(--white);font-family:"Tinos",serif;font-weight:700;line-height:1}
  .brand .name{font-size:40px;letter-spacing:1px;display:block}
  .brand .sub{font-size:14px;letter-spacing:3px;display:block;margin-top:4px}
  .contact{left:288px;top:122px;width:287px;text-align:center;color:var(--white);font-family:"Arimo",sans-serif;font-weight:700;font-size:12px;line-height:14px}
  .contact p+p{margin-top:14px}
  .phone{left:288px;top:204px;width:287px;text-align:center;color:var(--white);font-family:"Arimo",sans-serif;font-weight:700;font-size:19px}
  .web-photo{left:288px;top:452px;width:287px;text-align:center;color:var(--white);font-family:"Arimo",sans-serif;font-size:13px}

  /* outside: front panel */
  .badge{left:774px;top:14px;width:78px;text-align:center;color:var(--white);font-family:"Tinos",serif;font-weight:700;line-height:1}
  .badge .name{font-size:20px;display:block}
  .badge .sub{font-size:8px;letter-spacing:1.5px;display:block;margin-top:3px}
  .tagline{left:590px;top:355px;width:260px;text-align:center;color:var(--ink);font-family:"Tinos",serif;font-weight:700;font-size:16.5px;line-height:20.5px;text-transform:uppercase}
  .web-front{left:590px;top:455px;width:230px;text-align:center;color:var(--ink);font-family:"Arimo",sans-serif;font-size:13px}

  /* inside: left panel */
  .ribbon{left:7px;color:var(--white);font-weight:700;font-size:10px;line-height:15px}
  .ribbon.one{top:253px}
  .ribbon.two{top:301px}
  .one-stop{left:20px;top:365px;width:280px;color:var(--white);font-size:15.8px;line-height:23px;text-transform:uppercase}

  /* inside: middle panel */
  .offer-title{left:338px;top:64px;color:var(--white);font-weight:700;font-size:14px}
  .offer-lead{left:338px;top:103px;width:236px;color:var(--white);font-size:14.3px;line-height:20.5px}
  .offer-list{left:338px;top:186px;width:240px;color:var(--white);font-weight:700;font-size:14.3px;line-height:20.8px;list-style:none}
  .offer-list li{position:relative;padding-left:18px}
  .offer-list li::before{content:"•";position:absolute;left:0}

  /* inside: services panel */
  .services-title{left:617px;top:14px;width:192px;text-align:center;color:var(--white);font-size:19px}
  .service-list{top:73px;list-style:none;color:var(--ink);font-size:11px;line-height:21.8px}
  .service-list li::before{content:"• ";font-size:8px;vertical-align:1px}
  .service-list.col-a{left:598px}
  .service-list.col-b{left:745px}
</style>
</head>
<body>

<!-- Outside spread -->
<section class="sheet outside">
  <svg class="art" width="863" height="490" viewBox="0 0 863 490">
    <defs>
      <linearGradient id="roofers" x1="0" y1="0" x2="1" y2="1">
        <stop offset="0" stop-color="#c9d3dc"/><stop offset=".45" stop-color="#c8564f"/><stop offset="1" stop-color="#b5322f"/>
      </linearGradient>
      <linearGradient id="house-tan" x1="0" y1="0" x2="0" y2="1">
        <stop offset="0" stop-color="#3e4650"/><stop offset=".45" stop-color="#8a6a4a"/><stop offset="1" stop-color="#b89a72"/>
      </linearGradient>
      <linearGradient id="house-stone" x1="0" y1="0" x2="1" y2="1">
        <stop offset="0" stop-color="#8fb2d6"/><stop offset=".35" stop-color="#4e5a4f"/><stop offset=".7" stop-color="#b48a62"/><stop offset="1" stop-color="#7c6656"/>
      </linearGradient>
    </defs>

    <!-- left panel -->
    <polygon points="0,0 288,0 288,75 126,47 0,75" fill="var(--navy)"/>
    <polygon points="140,0 288,0 288,40 180,20" fill="var(--blue)"/>
    <polygon points="0,75 126,47 288,75 288,235 0,235" fill="url(#roofers)" role="img" aria-label="Photo: two roofers installing a red metal roof"/>
    <polygon points="20,300 57,300 76,332 57,364 20,364 1,332" fill="var(--pale)" opacity=".55"/>
    <polygon points="80,307 110,307 125,333 110,358 80,358 65,333" fill="var(--pale)" opacity=".6"/>
    <polygon points="25,390 50,390 70,420 50,450 25,450 5,420" fill="var(--pale)" opacity=".55"/>
    <polyline points="274,200 274,312 246,327" fill="none" stroke="var(--navy)" stroke-width="3"/>
    <line x1="274" y1="178" x2="274" y2="192" stroke="var(--navy)" stroke-width="3"/>

    <!-- cover contact panel -->
    <rect x="288" y="0" width="287" height="490" fill="var(--blue)"/>
    <polyline points="387,9 303,9 303,52" fill="none" stroke="var(--white)" stroke-width="3"/>
    <line x1="303" y1="60" x2="303" y2="72" stroke="var(--white)" stroke-width="3"/>
    <polygon points="288,292 395,240 575,262 575,490 288,490" fill="url(#house-tan)" role="img" aria-label="Photo: two-storey home with dark shingle roof and stone front"/>
    <polygon points="288,292 395,240 300,300" fill="var(--navy)" opacity=".6"/>
    <polygon points="420,205 575,300 730,345 575,262" fill="var(--navy)" opacity=".85"/>
    <line x1="564" y1="145" x2="564" y2="160" stroke="var(--white)" stroke-width="3"/>
    <line x1="564" y1="168" x2="564" y2="248" stroke="var(--white)" stroke-width="3"/>

    <!-- front panel -->
    <rect x="575" y="0" width="288" height="345" fill="url(#house-stone)" role="img" aria-label="Photo: stucco and stone house with green shingle roof"/>
    <polygon points="575,255 730,345 863,222 863,345 575,345" fill="var(--navy)"/>
    <polygon points="575,318 760,340 863,308 863,490 575,490" fill="var(--white)"/>
    <polygon points="592,300 628,300 648,335 628,370 592,370 575,335" fill="var(--pale)" opacity=".6"/>
    <polygon points="800,410 840,410 863,445 840,480 800,480 780,445" fill="var(--pale)" opacity=".7"/>
    <polygon points="774,0 852,0 852,70 813,88 774,70" fill="var(--navy)"/>
    <line x1="587" y1="301" x2="587" y2="380" stroke="var(--navy)" stroke-width="3"/>
    <line x1="587" y1="390" x2="587" y2="412" stroke="var(--navy)" stroke-width="3"/>
    <line x1="852" y1="387" x2="852" y2="405" stroke="var(--navy)" stroke-width="3"/>
    <polyline points="852,420 852,477 762,477" fill="none" stroke="var(--navy)" stroke-width="3"/>
  </svg>

  <div class="txt intro">
    <p>We provide a wide range of roofing services for all residential properties, including:</p>
    <ul>
      <li>- Single-family</li>
      <li>- Multi-family</li>
      <li>- Single-level</li>
      <li>- Multi-level</li>
      <li>- And more</li>
    </ul>
  </div>
  <p class="txt intro-note">Regardless of roof type, square footage, or extent of damage, our professional contractors are fully-equipped and ready to manage any project.</p>

  <div class="txt brand"><span class="name">TKB</span><span class="sub">ROOFING</span></div>
  <div class="txt contact">
    <p>1180 Maple Crest Drive<br>Carmel, IN 46032</p>
    <p>Open Monday - Saturday<br>8:00 am - 8:00 pm</p>
  </div>
  <p class="txt phone">317-555-0148</p>
  <p class="txt web-photo">www.tkbroofing-example.com</p>

  <div class="txt badge"><span class="name">TKB</span><span class="sub">ROOFING</span></div>
  <h1 class="txt tagline">Residential roofing solutions that works for you</h1>
  <p class="txt web-front">www.tkbroofing-example.com</p>
</section>

<!-- Inside spread -->
<section class="sheet inside">
  <svg class="art" width="882" height="500" viewBox="0 0 882 500">
    <defs>
      <linearGradient id="slate" x1="0" y1="0" x2="1" y2="1">
        <stop offset="0" stop-color="#9aa3ad"/><stop offset=".4" stop-color="#4b5666"/><stop offset="1" stop-color="#a9b2bd"/>
      </linearGradient>
      <linearGradient id="brick" x1="0" y1="0" x2="0" y2="1">
        <stop offset="0" stop-color="#9a4a40"/><stop offset=".6" stop-color="#7d342d"/><stop offset="1" stop-color="#5a6a3c"/>
      </linearGradient>
    </defs>

    <!-- left panel -->
    <rect x="0" y="80" width="300" height="316" fill="url(#slate)" role="img" aria-label="Photo: roofer in hard hat laying grey slate shingles"/>
    <polygon points="239,0 379,0 301,48" fill="var(--cyan)"/>
    <polygon points="0,142 300,396 420,500 0,500" fill="var(--navy)"/>
    <polyline points="109,17 17,17 17,85" fill="none" stroke="var(--navy)" stroke-width="3"/>
    <line x1="17" y1="93" x2="17" y2="108" stroke="var(--navy)" stroke-width="3"/>
    <polygon points="0,253 173,253 184,266 173,280 0,280" fill="var(--cyan)"/>
    <polygon points="0,299 232,299 246,334 0,334" fill="var(--cyan)"/>

    <!-- middle panel -->
    <polygon points="300,0 588,0 588,338 340,432 300,396" fill="var(--blue)"/>
    <polygon points="340,432 667,317 520,400" fill="var(--cyan)"/>

    <!-- services panel -->
    <polygon points="617,0 809,0 694,65" fill="var(--navy)"/>
    <polygon points="488,500 488,395 560,372 640,345 720,372 796,395 796,500" fill="url(#brick)" role="img" aria-label="Photo: large red brick family home"/>
    <polygon points="667,317 882,374 882,470 790,360" fill="var(--navy)"/>
    <polygon points="640,345 667,317 740,336" fill="var(--blue)"/>
    <line x1="869" y1="256" x2="869" y2="268" stroke="var(--navy)" stroke-width="3"/>
    <line x1="869" y1="276" x2="869" y2="372" stroke="var(--navy)" stroke-width="3"/>
  </svg>

  <p class="txt ribbon one">We also provide residential<br>siding repair and installation</p>
  <p class="txt ribbon two">Specialize primarily in vinyl, shake,<br>and cement fiber siding systems.</p>
  <p class="txt one-stop">TKB Roofing is truly your one-stop-shop for roofing and siding repair, replacement, installation, inspection, and more!</p>

  <h2 class="txt offer-title">We Give More to Our Clients</h2>
  <p class="txt offer-lead">To make the home remodeling process easy and convenient for our clients, we also offer:</p>
  <ul class="txt offer-list">
    <li>Free over-the-phone quotes,</li>
    <li>Free in-home consultations,</li>
    <li>Written Estimates,</li>
    <li>2 year workmanship warranties,</li>
    <li>and generous cash rewards for client referrals.</li>
  </ul>

  <h2 class="txt services-title">Services</h2>
  <ul class="txt service-list col-a">
    <li>Roof Repair</li><li>Roof Installation</li><li>Roof Inspection</li><li>Shingle Roofs</li><li>Asphalt Roofs</li><li>Metal Roofs</li><li>Flashing</li><li>Siding Replacement</li><li>Gutter Replacement</li><li>Ridge Vents</li>
  </ul>
  <ul class="txt service-list col-b">
    <li>Roof Replacement</li><li>Storm Damage Repair</li><li>Flat Roofs</li><li>Rubber Roofs</li><li>Pitched Roofs</li><li>Pipe Boots</li><li>Siding Repair</li><li>Siding Installation</li><li>Skylights</li>
  </ul>
</section>

</body>
</html>
```